Local Roofing/Construction company business needs new biz card design

We need a new business card design, current cards are from the start of this operation and generic at best. We are a local Construction Company (General Contractor) with a majority of our work originating from insurance claims-exterior finish work is the main focus (Roofs-Siding-Gutters etc). Heavily involved with homeowners and the low ball offers they receive from insurance company's after a insurable event takes place. I have attached some of our original logo file(s) below.

```html
<!DOCTYPE html>
<html lang="en">
<head>
<meta charset="utf-8">
<title>Stonefield Construction – Business Card</title>
<link rel="stylesheet" href="https://fonts.googleapis.com/css2?family=Open+Sans:wght@400;600;700&display=swap">
<style>
  :root {
    --backdrop: #232323;
    --card: #061b21;
    --green: #48b964;
    --white: #f1f4f3;
    --silver: #9aa6a8;
    --pattern-dark: #0c2a31;
    --pattern-mid: #2f4a50;
    --pattern-light: #c9cfd0;
    --plate-edge: #1c3a41;
  }
  * { box-sizing: border-box; margin: 0; padding: 0; }
  html, body {
    width: 1200px; height: 780px; overflow: hidden;
    background: var(--backdrop);
    font-family: "Open Sans", Arial, sans-serif;
  }
  .canvas { position: relative; width: 1200px; height: 780px; }

  .card {
    position: absolute;
    background: var(--card);
    border-radius: 4px;
    box-shadow: 0 18px 40px rgba(0,0,0,.45);
    overflow: hidden;
  }

  .brand-name {
    font-weight: 700; letter-spacing: .06em;
    text-transform: uppercase; line-height: 1; white-space: nowrap;
  }

  /* Front: portrait */
  .card-front { left: 110px; top: 110px; width: 330px; height: 560px; }
  .front-brand {
    position: absolute; left: 22px; top: 22px; width: 286px; height: 62px;
    border: 1px solid var(--plate-edge);
    border-radius: 4px;
    background: linear-gradient(135deg, #0a232a 0%, #12323a 70%, #3a4d52 100%);
    display: flex; align-items: center; padding: 0 18px;
  }
  .front-brand .brand-name { font-size: 15px; color: var(--silver); }
  .front-accent {
    position: absolute; right: 0; top: 300px; width: 14px; height: 70px;
    background: var(--green);
  }
  .contact {
    position: absolute; right: 34px; top: 290px; text-align: right; color: var(--white);
  }
  .person-name { font-size: 26px; font-weight: 700; line-height: 1.1; }
  .person-name .first { color: var(--green); }
  .person-title { font-size: 14px; margin-top: 4px; }
  .address { font-size: 13px; line-height: 1.4; margin-top: 14px; }
  .contact-list { list-style: none; margin-top: 14px; font-size: 12.5px; line-height: 1.75; }
  .contact-list li { display: flex; justify-content: flex-end; align-items: center; gap: 8px; }
  .contact-list svg { width: 13px; height: 13px; fill: var(--green); flex: none; }

  /* Back: landscape */
  .card-back { left: 510px; top: 225px; width: 560px; height: 330px; }
  .back-pattern {
    position: absolute; inset: 0;
    background: linear-gradient(100deg, var(--card) 0%, var(--pattern-dark) 50%, var(--pattern-mid) 80%, var(--pattern-light) 100%);
    opacity: .9;
  }
  .back-brand {
    position: absolute; left: 190px; top: 226px;
    display: flex; align-items: center; gap: 8px;
  }
  .back-brand .mark { width: 16px; height: 16px; background: var(--green); flex: none; }
  .back-brand .brand-name { color: var(--green); font-size: 15px; }
</style>
</head>
<body>
<main class="canvas">

  <section class="card card-front" aria-label="Business card front">
    <div class="front-brand">
      <span class="brand-name">Stonefield Construction</span>
    </div>
    <div class="front-accent"></div>
    <div class="contact">
      <h1 class="person-name"><span class="first">Lena</span> Haskell</h1>
      <p class="person-title">Managing Director</p>
      <p class="address">42 Orchard Bend Rd<br>Millbrook, MO 63010</p>
      <ul class="contact-list">
        <li>555-201-4478
          <svg viewBox="0 0 24 24"><path d="M6.6 10.8a15 15 0 0 0 6.6 6.6l2.2-2.2a1 1 0 0 1 1-.25 11 11 0 0 0 3.6.57 1 1 0 0 1 1 1V20a1 1 0 0 1-1 1A17 17 0 0 1 3 4a1 1 0 0 1 1-1h3.5a1 1 0 0 1 1 1 11 11 0 0 0 .57 3.6 1 1 0 0 1-.25 1z"/></svg></li>
        <li>555-201-9932 (Emergency)
          <svg viewBox="0 0 24 24"><path d="M6.6 10.8a15 15 0 0 0 6.6 6.6l2.2-2.2a1 1 0 0 1 1-.25 11 11 0 0 0 3.6.57 1 1 0 0 1 1 1V20a1 1 0 0 1-1 1A17 17 0 0 1 3 4a1 1 0 0 1 1-1h3.5a1 1 0 0 1 1 1 11 11 0 0 0 .57 3.6 1 1 0 0 1-.25 1z"/></svg></li>
        <li>www.stonefieldbuild.com
          <svg viewBox="0 0 24 24"><circle cx="12" cy="12" r="10" fill="none" stroke="#48b964" stroke-width="2"/><path d="M2 12h20M12 2c3 3 3 17 0 20M12 2c-3 3-3 17 0 20" fill="none" stroke="#48b964" stroke-width="1.6"/></svg></li>
        <li>hello@stonefieldbuild.com
          <svg viewBox="0 0 24 24"><path d="M2 6h20v12H2z" fill="none" stroke="#48b964" stroke-width="2"/><path d="M2 6l10 7 10-7" fill="none" stroke="#48b964" stroke-width="2"/></svg></li>
      </ul>
    </div>
  </section>

  <section class="card card-back" aria-label="Business card back">
    <div class="back-pattern" role="img" aria-label="Repeating brand monogram pattern fading from dark teal to silver"></div>
    <div class="back-brand">
      <span class="mark"></span>
      <span class="brand-name">Stonefield Construction</span>
    </div>
  </section>

</main>
</body>
</html>
```